Clean professional design needed for landscape property business

We need a logo for a new lawncare, landscaping , property maintenance business called Meadow Trim.
Our services include lawn mowing, garden maintenance, clean ups and some property maintenance.
We want a double sided business card that is clean and very professional using the colour scheme from our logo which is provided.
the business card should have impact as we will use these to drop into people's letterboxes as a marketing drop.
Initially we want to see what you come up with so there is a very wide scope here to work with.
Updates

Project Deadline Extended
Reason: we feel our original deadline was too short. we have extended to give more time for quality submissions.

Target Market(s)

High end property owners who don't wish to do there own gardneing or property maintenance

Industry/Entity Type

Business

Contact Information for Business Card

Name
Postion/ Title
Phone number
mobile
web address
physical address

services offered

Font styles to use
Sans Serif

Requirements
Must have
• curved edges preferrred
Nice to have
• We like the idea of the logo being embossed or etched into the card so it looks like it is below the surface of the card
Should not have
• No stock images or characters.

```html
<!DOCTYPE html>
<html lang="en">
<head>
<meta charset="utf-8">
<title>Meadow Trim – Business Card</title>
<link rel="stylesheet" href="https://fonts.googleapis.com/css2?family=Open+Sans:wght@400;600;700;800&display=swap">
<style>
  :root {
    --backdrop: #e6e6e6;
    --charcoal: #58595b;
    --lawn: #7dbe1f;
    --lawn-light: #b9de7d;
    --white: #ffffff;
    --ink: #1e1e1e;
    --card-radius: 20px;
  }
  * { margin: 0; padding: 0; box-sizing: border-box; }
  html, body {
    width: 1200px; height: 987px; overflow: hidden;
    background: var(--backdrop);
    font-family: "Open Sans", sans-serif;
  }
  .card {
    position: absolute; left: 293px; width: 615px; height: 350px;
    border-radius: var(--card-radius); overflow: hidden;
    box-shadow: 0 2px 6px rgba(0,0,0,0.18);
  }
  .card--front { top: 130px; background: var(--charcoal); color: var(--white); }
  .card--back { top: 506px; background: var(--white); }

  .front-accent { position: absolute; inset: 0; width: 100%; height: 100%; }

  .wordmark { font-weight: 800; letter-spacing: -1.5px; line-height: 1; }
  .card--front .wordmark {
    position: absolute; left: 33px; top: 40px; font-size: 46px; color: var(--white);
  }
  .person { position: absolute; left: 33px; top: 118px; }
  .person__name { font-size: 20px; font-weight: 700; letter-spacing: 0.3px; line-height: 1.2; }
  .person__title { font-size: 15px; line-height: 1.3; }
  .address { position: absolute; left: 33px; top: 174px; font-size: 15px; line-height: 1.45; }
  .contacts { position: absolute; left: 33px; top: 227px; list-style: none; font-size: 15px; }
  .contacts li { display: flex; align-items: center; height: 24px; }
  .contacts svg { width: 14px; height: 14px; margin-right: 9px; fill: var(--white); flex: none; }

  .card--back .brand {
    position: absolute; left: 0; right: 0; top: 96px;
    display: flex; justify-content: center; align-items: center; gap: 14px;
  }
  .card--back .wordmark { font-size: 50px; color: var(--charcoal); }
  .brand__square { width: 26px; height: 26px; background: var(--lawn); }

  .lawn-art {
    position: absolute; left: 0; right: 0; top: 172px; bottom: 0;
    background: linear-gradient(to bottom, var(--white) 0%, var(--lawn-light) 30%, var(--lawn) 62%, var(--lawn) 100%);
  }
  .services {
    position: absolute; left: 0; right: 0; top: 290px;
    text-align: center; font-size: 15px; line-height: 1.35; color: var(--ink);
  }
  .services .dot { font-size: 12px; vertical-align: 1px; padding: 0 2px; }
</style>
</head>
<body>

<section class="card card--front" aria-label="Business card front">
  <svg class="front-accent" viewBox="0 0 615 350" preserveAspectRatio="none" aria-hidden="true">
    <path d="M585 0 L615 0 L615 350 L440 350 C545 330 600 240 585 0 Z" fill="var(--lawn)"/>
  </svg>
  <div class="wordmark">Meadow Trim</div>
  <div class="person">
    <p class="person__name">DANIEL HART</p>
    <p class="person__title">CEO &amp; Founder</p>
  </div>
  <address class="address" style="font-style:normal">
    4120 Willow Bend Road<br>
    Fairbanks, Alaska 34812
  </address>
  <ul class="contacts">
    <li><svg viewBox="0 0 24 24"><path d="M6.6 10.8a15.1 15.1 0 0 0 6.6 6.6l2.2-2.2a1 1 0 0 1 1-.25 11.4 11.4 0 0 0 3.6.6 1 1 0 0 1 1 1V20a1 1 0 0 1-1 1A17 17 0 0 1 3 4a1 1 0 0 1 1-1h3.5a1 1 0 0 1 1 1c0 1.25.2 2.45.6 3.6a1 1 0 0 1-.25 1z"/></svg>(555) 214-3087</li>
    <li><svg viewBox="0 0 24 24"><path d="M7 1h10a2 2 0 0 1 2 2v18a2 2 0 0 1-2 2H7a2 2 0 0 1-2-2V3a2 2 0 0 1 2-2zm0 3v14h10V4z"/></svg>(555) 709-6152</li>
    <li><svg viewBox="0 0 24 24"><path d="M2 5h20v14H2z M2 5l10 8 10-8" fill="none" stroke="#fff" stroke-width="2"/></svg>dan@meadowtrim.com</li>
    <li><svg viewBox="0 0 24 24"><circle cx="12" cy="12" r="10"/><path d="M2 12h20M12 2c3 3 3 17 0 20M12 2c-3 3-3 17 0 20" stroke="var(--charcoal)" stroke-width="1.5" fill="none"/></svg>www.meadowtrim.com</li>
  </ul>
</section>

<section class="card card--back" aria-label="Business card back">
  <div class="lawn-art" role="img" aria-label="Illustration of a strip of green lawn grass along the bottom of the card"></div>
  <div class="brand">
    <span class="wordmark">Meadow Trim</span>
    <span class="brand__square" aria-hidden="true"></span>
  </div>
  <p class="services">
    <span class="dot">●</span> Lawn Mowing <span class="dot">●</span> Garden Maintenance<br>
    Clean ups &amp; Some Property Maintenance.
  </p>
</section>

</body>
</html>
```